RM BIZ CARDS

Hi,

Is it possible to see a one sided version (with logo and info) as well as a two-sided version (front side w/logo and back side with info)?
How do we choose card stock and finish once we approve a design?

We would like the following info included:

Peter Lowell
Rosfeld Talent Media
4127 Marwick Lane, Suite 300
Los Angeles, CA 90041
(323) 555-0148
peter@rosfeldtalentmedia.example

```html
<!DOCTYPE html>
<html lang="en">
<head>
<meta charset="utf-8">
<title>Rosfeld Talent Media – Business Card</title>
<link rel="stylesheet" href="https://fonts.googleapis.com/css2?family=Questrial&display=swap">
<style>
  :root {
    --page-bg: #d8d1c8;
    --frost-light: #f4f5f7;
    --frost-mid: #e4e6ea;
    --frost-warm: #eadfe0;
    --panel-dark: #050505;
    --panel-edge: #1b1b1b;
    --ink-dark: #1d1b1b;
    --gold: #cdb78e;
    --gold-soft: #bfae8f;
    --text-muted: #cfc6b7;
  }
  * { margin: 0; padding: 0; box-sizing: border-box; }
  html, body {
    width: 1200px;
    height: 970px;
    overflow: hidden;
    background: var(--page-bg);
    font-family: "Questrial", sans-serif;
  }
  .card {
    position: absolute;
    left: 80px;
    top: 190px;
    width: 1040px;
    height: 590px;
    border-radius: 26px;
    overflow: hidden;
    display: flex;
    box-shadow: 0 18px 40px rgba(0,0,0,0.18);
  }
  .card-front {
    width: 520px;
    height: 100%;
    background:
      linear-gradient(180deg, var(--frost-light) 0%, var(--frost-mid) 55%, var(--frost-warm) 78%, var(--frost-mid) 100%);
    display: flex;
    align-items: center;
    justify-content: center;
  }
  .brand-name {
    margin-top: 150px;
    font-size: 44px;
    letter-spacing: 4px;
    color: var(--ink-dark);
    white-space: nowrap;
  }
  .card-back {
    width: 520px;
    height: 100%;
    background: linear-gradient(160deg, var(--panel-edge) 0%, var(--panel-dark) 35%, var(--panel-dark) 100%);
    padding: 174px 0 0 56px;
  }
  .person-name {
    font-size: 29px;
    letter-spacing: 0.5px;
    color: var(--gold);
    line-height: 1.1;
  }
  .company {
    font-size: 22px;
    color: var(--gold-soft);
    margin-top: 4px;
  }
  .address {
    margin-top: 30px;
    font-size: 24px;
    letter-spacing: 1px;
    line-height: 33px;
    color: var(--text-muted);
  }
  .contact-list {
    list-style: none;
    margin-top: 24px;
  }
  .contact-item {
    display: flex;
    align-items: center;
    gap: 12px;
    height: 35px;
    font-size: 21px;
    color: var(--text-muted);
    white-space: nowrap;
  }
  .contact-item.email { color: var(--gold-soft); }
  .contact-icon { width: 30px; height: 30px; flex: none; }
</style>
</head>
<body>
  <div class="card">
    <section class="card-front">
      <div class="brand-name">ROSFELD TALENT</div>
    </section>
    <section class="card-back">
      <div class="person-name">PETER LOWELL</div>
      <div class="company">Rosfeld Talent Media</div>
      <div class="address">
        4127 Marwick Lane, Suite 300<br>
        Los Angeles, CA 90041
      </div>
      <ul class="contact-list">
        <li class="contact-item phone">
          <svg class="contact-icon" viewBox="0 0 30 30" aria-hidden="true">
            <circle cx="15" cy="15" r="13" fill="none" stroke="#cdb78e" stroke-width="1.6"/>
            <path d="M8 12 Q15 6 22 12 L20 14 L17 12 L13 12 L10 14 Z" fill="#cdb78e"/>
            <rect x="10" y="15" width="10" height="7" rx="1" fill="#cdb78e"/>
          </svg>
          <span>(323) 555-0148</span>
        </li>
        <li class="contact-item email">
          <svg class="contact-icon" viewBox="0 0 30 30" aria-hidden="true">
            <circle cx="15" cy="15" r="13" fill="none" stroke="#cdb78e" stroke-width="1.6"/>
            <rect x="8.5" y="10" width="13" height="10" fill="#cdb78e"/>
            <path d="M8.5 10 L15 15.5 L21.5 10" fill="none" stroke="#050505" stroke-width="1.2"/>
          </svg>
          <span>peter@rosfeldtalentmedia.example</span>
        </li>
      </ul>
    </section>
  </div>
</body>
</html>
```